Clarinet Past Midnight: mini recital & soiree

I need a poster design for a recital I'm doing next Friday April 25. It's an "after party" from 10 - 1am where I'll be playing a 30 min program followed by a DJ and there'll be food wine etc. I want to see a very "sexy" kind of poster. Modern with a "south beach" kind of art deco feel but without the really cheesy connotation that south beach sometimes has (if that makes any sense). I've included the link for the Facebook event so you can get an idea of the feel I want.

Cheers!

https://www.gatherloop.example/events/315907264810356/

Target Market(s)

College Students at the Coralwind State College

South Beach-ians

Industry/Entity Type

Events

Colors

Designer to choose colors to be used in the design.

Requirements
Must have
• Title of event..
Date..
Location..
Food / Beverage served..
DJ Verbosky..

```html
<!DOCTYPE html>
<html lang="en">
<head>
<meta charset="utf-8">
<title>Clarinet Past Midnight — After Party</title>
<link rel="stylesheet" href="https://fonts.googleapis.com/css2?family=Poiret+One&family=Questrial&family=Julius+Sans+One&display=swap">
<style>
  :root {
    --ink: #0d0c0b;
    --night: #161412;
    --disc: #1c1915;
    --cream: #f3e6cc;
    --gold: #c9a772;
    --grey: #d6d3cc;
    --sunset-hi: #f0a24a;
    --sunset-mid: #c5621f;
    --sunset-lo: #4a2410;
  }
  * { margin: 0; padding: 0; box-sizing: border-box; }
  html, body { width: 900px; height: 1200px; overflow: hidden; background: var(--ink); }
  .poster { position: relative; width: 900px; height: 1200px; overflow: hidden; background: var(--night); }
  .crowd-collage {
    position: absolute; inset: 0;
    background:
      radial-gradient(ellipse at 20% 30%, rgba(120, 90, 60, .35), transparent 55%),
      radial-gradient(ellipse at 80% 70%, rgba(110, 85, 60, .3), transparent 55%),
      linear-gradient(180deg, #2a241d 0%, #1d1915 50%, #141210 100%);
  }
  .shapes { position: absolute; inset: 0; }
  .after-party, .title, .tagline, .date, .city, .dj, .venue {
    position: absolute; left: 0; width: 900px; text-align: center; color: var(--cream);
  }
  .after-party { top: 368px; left: -10px; font-family: "Poiret One", sans-serif; font-size: 30px; letter-spacing: .04em; }
  .title { top: 418px; left: 0; font-family: "Questrial", sans-serif; font-size: 76px; letter-spacing: .26em; text-indent: .26em; }
  .tagline { top: 500px; left: -4px; font-family: "Julius Sans One", sans-serif; font-size: 13px; letter-spacing: .28em; }
  .date { top: 530px; left: -10px; font-family: "Questrial", sans-serif; font-size: 36px; font-variant: small-caps; color: var(--cream); }
  .city { top: 595px; left: -8px; font-family: "Julius Sans One", sans-serif; font-size: 13px; letter-spacing: .3em; }
  .dj { top: 618px; left: 620px; width: 150px; font-family: "Questrial", sans-serif; font-size: 24px; line-height: 1.5; font-variant: small-caps; }
  .dj span { display: block; font-size: 32px; }
  .venue { top: 795px; left: 12px; font-family: "Questrial", sans-serif; font-size: 15.5px; letter-spacing: .13em; line-height: 28px; color: var(--grey); text-transform: uppercase; }
  .venue .stars { color: var(--cream); font-size: 15px; letter-spacing: .25em; margin-bottom: 4px; }
  .client-mark { position: absolute; top: 962px; left: 0; width: 900px; display: flex; justify-content: center; align-items: center; gap: 8px; font-family: "Questrial", sans-serif; font-size: 14px; letter-spacing: .2em; color: var(--gold); text-transform: uppercase; }
  .client-mark i { width: 12px; height: 12px; background: var(--gold); display: inline-block; }
  .curved { font-family: "Questrial", sans-serif; fill: var(--cream); }
</style>
</head>
<body>
<main class="poster">
  <div class="crowd-collage" role="img" aria-label="Collage of nightclub photos of guests dancing and a singer at a microphone"></div>

  <svg class="shapes" width="900" height="1200" viewBox="0 0 900 1200">
    <defs>
      <linearGradient id="sunset" x1="0" y1="0" x2="0" y2="1">
        <stop offset="0" stop-color="var(--sunset-mid)"/>
        <stop offset=".45" stop-color="var(--sunset-hi)"/>
        <stop offset=".75" stop-color="var(--sunset-mid)"/>
        <stop offset="1" stop-color="var(--sunset-lo)"/>
      </linearGradient>
      <path id="food-arc" d="M333,615 A190,190 0 0 0 550,635"/>
      <path id="live-arc" d="M275,684 A280,280 0 0 0 603,707"/>
    </defs>
    <circle class="lower-disc" cx="460" cy="790" r="225" fill="var(--disc)" opacity=".95"/>
    <circle class="ring" cx="455" cy="505" r="322" fill="var(--disc)"/>
    <circle class="sunset" cx="455" cy="490" r="290" fill="url(#sunset)" role="img" aria-label="Tropical sunset over the sea with a palm frond"/>
    <circle class="dj-badge" cx="695" cy="680" r="78" fill="var(--disc)"/>
    <text class="curved" font-size="14" letter-spacing="2"><textPath href="#food-arc" startOffset="50%" text-anchor="middle">FOOD, DRINKS, WINE</textPath></text>
    <text class="curved" font-size="23" fill="var(--gold)" style="font-variant: small-caps; fill: var(--gold)"><textPath href="#live-arc" startOffset="50%" text-anchor="middle">Clarinet Live Preformance</textPath></text>
  </svg>

  <p class="after-party">AFTER PARTY</p>
  <h1 class="title">CLARINET</h1>
  <p class="tagline">CLARINET PAST MIDNIGHT: MINI RECITAL &amp; SOIRÉE</p>
  <p class="date">Friday; 25.04.2014</p>
  <p class="city">MIAMI 2014</p>
  <p class="dj">DJ<span>Verbosky</span></p>

  <address class="venue" style="font-style: normal">
    <div class="stars">★★★</div>
    Halvorsen Alumni Center-<br>
    Coralwind State College<br>
    4870 Tidewater Lane,<br>
    Palm Harbor Bay, Florida 33990
  </address>

  <div class="client-mark"><i></i>Coralwind</div>
</main>
</body>
</html>
```